Torvin Home care non-medical home care brochure

Develop a eye catching non-medical Homecare brochure, detailing services we provide. Services
Personal Care Attendants
Extended Care Attendants
Non-Medical Transportation
We accept
Calvora Wellcare
Long Term Care Insurance Plans
Private Pay

HELP WITH:
Eating
Bathing
Dressing
Grooming
Moving from one surface to another
Walking or using a wheelchair
Toileting
Changing positions in bed
OTHER SERVICES:
Light housekeeping
Preparing and storing meals
Shopping
Laundry
Reminders about taking medicines
Help with medical appointments
Help finding transportation for appts.

Target Market(s)

Seniors and individuals needing non-medical assistance.

Industry/Entity Type

Health Care

Font styles to use
Sans Serif

Requirements
Must have
• Details regarding services, tri-fold design
Nice to have
• Logo, details detailng services
Should not have
• n/a

```html
<!DOCTYPE html>
<html lang="en">
<head>
<meta charset="utf-8">
<title>Torvin Home Care Tri-fold Brochure</title>
<link rel="stylesheet" href="https://fonts.googleapis.com/css2?family=Montserrat:ital,wght@0,400;0,500;0,600;0,700;0,800;1,400&display=swap">
<style>
:root{
  --navy:#2b2d52;
  --red:#e1222a;
  --white:#ffffff;
  --paper:#fbfbfb;
  --stage:#e3e3e5;
  --ink:#3a3a48;
}
*{box-sizing:border-box;margin:0;padding:0}
html,body{width:1200px;height:2400px;overflow:hidden}
body{background:var(--stage);font-family:'Montserrat',sans-serif;color:var(--ink);position:relative}
.sheet{position:absolute;left:45px;width:1110px;height:858px;background:var(--paper);box-shadow:0 10px 30px rgba(0,0,0,.15);overflow:hidden}
.sheet--outer{top:230px}
.sheet--inner{top:1310px}
.sheet-art{position:absolute;inset:0;width:1110px;height:858px}
.block{position:absolute}
.section-title{font-weight:800;color:var(--navy);text-transform:uppercase;line-height:1.1}
.rule{display:block;width:70px;height:4px;background:var(--red);margin:8px 0 12px}
.body-copy{font-size:12px;line-height:1.6;color:var(--ink)}
.about{left:30px;top:34px;width:315px}
.about .section-title{font-size:26px}
.contact{left:370px;top:300px;width:370px;text-align:center;color:var(--white)}
.contact-icons{display:flex;justify-content:center;gap:8px;margin-bottom:26px}
.contact-icons svg{width:40px;height:40px}
.contact-line{font-size:14px;line-height:1.5;margin-bottom:10px}
.brand{left:740px;top:540px;width:370px;display:flex;align-items:center;justify-content:center;gap:12px;color:var(--navy);font-weight:700}
.brand-mark{width:20px;height:20px;background:var(--red)}
.brand-name{font-size:34px;line-height:1;letter-spacing:1px}
.brand-name small{display:block;font-size:15px;letter-spacing:6px;margin-top:4px}
.headline{left:740px;top:640px;width:370px;text-align:center;font-weight:800;font-size:29px;line-height:1.15;text-transform:uppercase}
.headline .line-navy{color:var(--navy);display:block}
.headline .line-red{color:var(--red);display:block}
.call-pill{position:absolute;height:50px;border-radius:25px;background:var(--navy);color:var(--white);font-weight:800;font-size:21px;display:flex;align-items:center;justify-content:center;gap:10px;text-transform:uppercase}
.call-pill .call-label{color:var(--red)}
.call-pill--cover{left:775px;top:760px;width:300px}
.service .section-title{font-size:20px}
.service--personal{left:28px;top:30px;width:215px}
.service--extended{left:28px;top:330px;width:320px}
.service--transport{left:28px;top:590px;width:320px}
.list-label{font-size:12px;letter-spacing:6px;text-transform:uppercase;color:var(--red);text-align:center;margin-bottom:10px}
.task-list{list-style:none;text-align:center}
.task-list li{font-size:12px;font-weight:600;text-transform:uppercase;line-height:1.25;padding:7px 0 6px;border-bottom:2px solid var(--red)}
.help-with{left:405px;top:340px;width:300px;color:var(--white)}
.other-services{left:775px;top:40px;width:300px;color:var(--navy)}
.brand--small{left:740px;top:440px;width:370px;gap:8px}
.brand--small .brand-mark{width:12px;height:12px}
.brand--small .brand-name{font-size:18px}
.brand--small .brand-name small{font-size:9px;letter-spacing:3px;margin-top:2px}
.accept{left:800px;top:510px;width:250px;text-align:center}
.accept .section-title{font-size:22px}
.accept .rule{margin:6px auto 10px}
.accept-list{list-style:none;color:var(--navy);font-weight:600;font-size:17px}
.accept-list li{padding:6px 0;border-bottom:2px dotted var(--navy)}
.accept-list li:last-child{border-bottom:none}
.call-pill--back{left:775px;top:770px;width:300px}
</style>
</head>
<body>

<section class="sheet sheet--outer">
  <svg class="sheet-art" viewBox="0 0 1110 858">
    <defs>
      <linearGradient id="careGrad" x1="0" y1="0" x2="1" y2="1">
        <stop offset="0" stop-color="#f2ede8"/><stop offset="1" stop-color="#d8c6b8"/>
      </linearGradient>
      <linearGradient id="handsGrad" x1="0" y1="0" x2="1" y2="1">
        <stop offset="0" stop-color="#c9d8e6"/><stop offset="1" stop-color="#e7c3a8"/>
      </linearGradient>
    </defs>
    <rect x="370" y="0" width="370" height="858" fill="var(--navy)"/>
    <polygon points="0,620 300,545 370,858 0,858" fill="var(--navy)"/>
    <polygon points="0,636 288,563 354,858 0,858" fill="var(--red)"/>
    <polygon points="0,646 280,575 342,858 0,858" fill="var(--white)"/>
    <polygon points="0,656 272,587 330,858 0,858" fill="url(#handsGrad)" role="img" aria-label="Photo of a caregiver holding an elderly person's hands"/>
    <polygon points="722,0 1110,0 1110,430 925,548 722,420" fill="var(--navy)"/>
    <polygon points="736,0 1110,0 1110,412 925,530 736,406" fill="var(--white)"/>
    <polygon points="744,0 1110,0 1110,402 925,520 744,398" fill="var(--red)"/>
    <polygon points="752,0 1110,0 1110,392 925,510 752,390" fill="url(#careGrad)" role="img" aria-label="Photo of a smiling caregiver embracing an elderly woman"/>
  </svg>

  <div class="block about">
    <h2 class="section-title">About Torvin<br>Homecare</h2>
    <span class="rule"></span>
    <p class="body-copy">Lorem ipsum dolor sit amet, consectetur adipiscing. Proin gravida nibh vel velit auctor aliquet. Aenean sollicitudin, lorem quis bibendum auctor, nisi elit consequat ipsum, nec sagittis sem nibh id elit. Duis sed odio sit amet nibh vulputate cursus a sit amet mauris. Morbi accumsan ipsum velit. Nam nec tellus a odio tincidunt auctor a ornare odio. Sed non mauris vitae erat consequat auctor eu in elit. Class aptent taciti sociosqu ad litora torquent per conubia nostra, per inceptos himenaeos. Mauris in erat justo. Nullam ac urna eu felis dapibus condimentum sit amet a augue.</p>
  </div>

  <div class="block contact">
    <div class="contact-icons">
      <svg viewBox="0 0 40 40"><circle cx="20" cy="20" r="19" fill="var(--red)"/><path d="M14 11c1-1 2-1 3 0l2 3c.6 1 .4 2-.4 2.6l-1 .8c.8 2 2.6 3.8 4.6 4.6l.8-1c.6-.8 1.6-1 2.6-.4l3 2c1 1 1 2 0 3l-1.4 1.4c-1.6 1.6-4.6.8-8.2-2.8S11 14 12.6 12.4z" fill="#fff"/></svg>
      <svg viewBox="0 0 40 40"><circle cx="20" cy="20" r="19" fill="var(--red)"/><rect x="10" y="13" width="20" height="14" rx="1.5" fill="#fff"/><path d="M10.5 14 20 21l9.5-7" fill="none" stroke="var(--red)" stroke-width="1.6"/></svg>
      <svg viewBox="0 0 40 40"><circle cx="20" cy="20" r="19" fill="var(--red)"/><path d="M20 9a7 7 0 0 1 7 7c0 5-7 14-7 14s-7-9-7-14a7 7 0 0 1 7-7z" fill="#fff"/><circle cx="20" cy="16" r="2.6" fill="var(--red)"/></svg>
      <svg viewBox="0 0 40 40"><circle cx="20" cy="20" r="19" fill="var(--red)"/><g fill="none" stroke="#fff" stroke-width="1.8"><circle cx="20" cy="20" r="9"/><ellipse cx="20" cy="20" rx="4" ry="9"/><path d="M11 20h18M12.5 15h15M12.5 25h15"/></g></svg>
    </div>
    <p class="contact-line">123 456 7890</p>
    <p class="contact-line">youremailaddresswillgoes@here</p>
    <p class="contact-line">12 youraddress, will goes here<br>dummy text now 4567</p>
    <p class="contact-line">www.torvinhomecare.com</p>
  </div>

  <div class="block brand">
    <span class="brand-mark"></span>
    <span class="brand-name">TORVIN<small>HOME CARE</small></span>
  </div>

  <h1 class="block headline">
    <span class="line-navy">Your Headline</span>
    <span class="line-red">Will Goes Here</span>
  </h1>

  <div class="call-pill call-pill--cover"><span class="call-label">Call us</span><span>123 456 7890</span></div>
</section>

<section class="sheet sheet--inner">
  <svg class="sheet-art" viewBox="0 0 1110 858">
    <defs>
      <linearGradient id="duoGrad" x1="0" y1="0" x2="1" y2="1">
        <stop offset="0" stop-color="#eee7e1"/><stop offset="1" stop-color="#d7bfb1"/>
      </linearGradient>
    </defs>
    <rect x="370" y="0" width="370" height="858" fill="var(--navy)"/>
    <polygon points="240,0 745,0 480,300" fill="var(--navy)"/>
    <polygon points="256,0 728,0 480,282" fill="var(--red)"/>
    <polygon points="266,0 716,0 480,270" fill="var(--white)"/>
    <polygon points="280,0 702,0 480,254" fill="url(#duoGrad)" role="img" aria-label="Photo of an elderly woman and her smiling caregiver cheek to cheek"/>
  </svg>

  <div class="block service service--personal">
    <h2 class="section-title">Personal Care<br>Attendants</h2>
    <span class="rule"></span>
    <p class="body-copy">Lorem ipsum dolor sit amet, consectetur adipiscing. Proin gravida nibh vel velit auctor aliquet. Aenean sollicitudin, lorem quis bibendum auctor, nisi elit consequat ipsum, nec sagittis sem nibh id elit. Duis sed odio sit amet nibh vulputate cursus a sit amet mauris.</p>
  </div>

  <div class="block service service--extended">
    <h2 class="section-title">Extended Care<br>Attendants</h2>
    <span class="rule"></span>
    <p class="body-copy">Lorem ipsum dolor sit amet, consectetur adipiscing. Proin gravida nibh vel velit auctor aliquet. Aenean sollicitudin, lorem quis bibendum auctor, nisi elit consequat ipsum, nec sagittis sem nibh id elit. Duis sed odio sit amet nibh vulputate cursus a sit amet mauris. Morbi accumsan ipsum velit. Nam nec tellus a odio tincidunt auctor a ornare odio. Sed non tincidunt.</p>
  </div>

  <div class="block service service--transport">
    <h2 class="section-title">Non-Medical<br>Transportation</h2>
    <span class="rule"></span>
    <p class="body-copy">Lorem ipsum dolor sit amet, consectetur adipiscing. Proin gravida nibh vel velit auctor aliquet. Aenean sollicitudin, lorem quis bibendum auctor, nisi elit consequat ipsum, nec sagittis sem nibh id elit. Duis sed odio sit amet nibh vulputate cursus a sit amet mauris. Morbi accumsan ipsum velit. Nam nec tellus a odio tincidunt auctor a ornare odio. Sed non tincidunt.</p>
  </div>

  <div class="block help-with">
    <p class="list-label">We help with</p>
    <ul class="task-list">
      <li>Eating</li>
      <li>Bathing</li>
      <li>Dressing</li>
      <li>Grooming</li>
      <li>Moving from one<br>surface to another</li>
      <li>Walking or using<br>a wheelchair</li>
      <li>Toileting</li>
      <li>Changing positions<br>in bed</li>
    </ul>
  </div>

  <div class="block other-services">
    <p class="list-label">Other services</p>
    <ul class="task-list">
      <li>Light housekeeping</li>
      <li>Preparing and storing meals</li>
      <li>Shopping</li>
      <li>Laundry</li>
      <li>Reminders about taking medicines</li>
      <li>Help with medical appointments</li>
      <li>Help finding transportation<br>for appts.</li>
    </ul>
  </div>

  <div class="block brand brand--small">
    <span class="brand-mark"></span>
    <span class="brand-name">TORVIN<small>HOME CARE</small></span>
  </div>

  <div class="block accept">
    <h2 class="section-title">We Accept</h2>
    <span class="rule"></span>
    <ul class="accept-list">
      <li>Calvora Wellcare</li>
      <li>Long Term Care<br>Insurance Plans</li>
      <li>Private Pay</li>
    </ul>
  </div>

  <div class="call-pill call-pill--back"><span class="call-label">Call us</span><span>123 456 7890</span></div>
</section>

</body>
</html>
```